Heronfield Wealth Advisors, Inc. Marketing Collateral - 401k Rollover Decisions

We are looking to create a branded one-pager marketing collateral piece talking about 401k Rollovers & the important information people should know. Rough draft of concept & content included below, and we will finalize copy later. Would include a call to action to contact us. Our website and other contact information are available at https://growwithheronfield.com/.

Target Market(s)

Working adults ages 55-75 with access to retirement accounts or who have a 401k account. Especially interested in appealing to people who work for small businesses, local businesses, have company stock, and other unique needs in this space.

Industry/Entity Type

Financial services

Font styles to use
Other font styles liked:
• Cambria

Requirements
Must have
• Clear message & call to action
Nice to have
• Highlight how many Americans have been changing jobs since COVID and why it would be worth working with a professional to make decisions on what to do with retirement accounts and assets. (We're working on getting that stat)
Should not have
• Too much text, don't want to inundate with text blocks

```html
<!DOCTYPE html>
<html lang="en">
<head>
<meta charset="utf-8">
<title>Heronfield Wealth Advisors – 401(k) Rollover Options</title>
<link href="https://fonts.googleapis.com/css2?family=Noto+Serif:wght@400;700&family=Open+Sans:wght@400;600;700&display=swap" rel="stylesheet">
<style>
  :root {
    --red: #c8212f;
    --ink: #1c1c1c;
    --muted-line: #e2e2e2;
    --paper: #ffffff;
    --stage: #e9e9e9;
    --gold: #e2b233;
    --cream: #f3ead8;
  }
  * { box-sizing: border-box; margin: 0; padding: 0; }
  html, body { width: 990px; height: 1200px; overflow: hidden; }
  body { background: var(--stage); font-family: "Open Sans", Arial, sans-serif; color: var(--ink); }

  .flyer { position: absolute; left: 45px; top: 17px; width: 900px; height: 1165px; background: var(--paper); overflow: hidden; }

  .hero-photo {
    position: absolute; left: 0; top: 0; width: 900px; height: 371px;
    background:
      radial-gradient(ellipse at 72% 55%, var(--cream) 0 18%, transparent 42%),
      linear-gradient(90deg, #ffffff 0%, #fbf7ee 38%, #f0d680 62%, var(--gold) 82%, #c79a22 100%);
  }
  .hero-rule { position: absolute; left: 0; top: 371px; width: 900px; height: 5px; background: var(--red); }

  .brand { position: absolute; left: 52px; top: 120px; width: 350px; text-align: center; color: var(--ink); font-family: "Noto Serif", Georgia, serif; font-weight: 400; }
  .brand-dot { display: block; width: 46px; height: 46px; border-radius: 50%; background: var(--red); margin: 0 auto 26px; }
  .brand-name { font-size: 46px; line-height: 1; letter-spacing: 1px; }
  .brand-sub { font-size: 18px; letter-spacing: 3px; margin-top: 8px; }

  .lead-box { position: absolute; left: 52px; top: 325px; width: 460px; height: 261px; background: var(--red); }
  .lead-box .bar { position: absolute; left: 47px; top: 36px; width: 3px; height: 186px; background: #fff; }
  .lead-text { position: absolute; left: 69px; top: 33px; width: 380px; color: #fff; font-family: "Noto Serif", Georgia, serif; font-weight: 700; font-size: 25px; line-height: 32px; }
  .lead-box .fold { position: absolute; right: 0; bottom: 0; width: 28px; height: 28px; }

  .body-copy { position: absolute; left: 52px; top: 613px; width: 460px; font-size: 12.6px; line-height: 18px; text-align: justify; }
  .body-copy p + p { margin-top: 10px; }

  .compare { position: absolute; left: 52px; top: 832px; width: 460px; }
  .compare-title { height: 49px; background: var(--red); color: #fff; font-family: "Noto Serif", Georgia, serif; font-weight: 700; font-size: 25px; line-height: 49px; text-align: center; border-radius: 2px 2px 0 0; }
  .compare-table { width: 100%; border-collapse: collapse; border: 1px solid var(--muted-line); table-layout: fixed; }
  .compare-table th { height: 40px; text-align: left; padding-left: 33px; font-size: 21px; font-weight: 700; background: linear-gradient(90deg, #e6e6e6, #fafafa); }
  .compare-table th:first-child { width: 253px; border-right: 2px solid #fff; }
  .compare-table td { vertical-align: top; padding: 6px 14px 4px 33px; font-size: 14px; line-height: 19.5px; border-top: 1px solid var(--muted-line); position: relative; }
  .compare-table td:first-child { border-right: 1px solid var(--muted-line); padding-right: 22px; }
  .compare-table td:last-child { padding-right: 30px; }
  .compare-table td svg { position: absolute; left: 15px; top: 10px; width: 12px; height: 12px; }
  .row-a { height: 52px; }
  .row-b { height: 73px; }
  .row-c { height: 75px; }

  .option { position: absolute; left: 541px; width: 306px; border: 1px solid var(--muted-line); border-radius: 3px; background: #fff; }
  .option h2 { height: 38px; background: var(--red); color: #fff; font-family: "Noto Serif", Georgia, serif; font-weight: 700; font-size: 27px; line-height: 38px; padding-left: 26px; border-radius: 3px 3px 0 0; margin: -1px -1px 0; }
  .option p { padding: 12px 40px 0 26px; font-size: 12.6px; line-height: 18px; }
  .opt-leave { top: 403px; height: 101px; }
  .opt-roll { top: 531px; height: 121px; }
  .opt-move { top: 679px; height: 141px; }
  .opt-move p { padding-top: 15px; }
  .opt-take { top: 846px; height: 137px; }
  .opt-take p { padding-top: 17px; }

  .cta { position: absolute; left: 541px; top: 1011px; width: 307px; height: 40px; }
  .cta-tab { position: absolute; left: 0; top: 0; }
  .cta-label { position: absolute; left: 26px; top: 0; color: #fff; font-family: "Noto Serif", Georgia, serif; font-weight: 700; font-size: 26px; line-height: 40px; }
  .phone { position: absolute; left: 568px; top: 1062px; display: flex; align-items: center; gap: 8px; font-size: 33px; font-weight: 700; letter-spacing: 0.3px; }
  .phone svg { width: 28px; height: 28px; }
  .website { position: absolute; left: 571px; top: 1108px; font-size: 16.5px; letter-spacing: 1.4px; }
  .website strong { color: var(--red); font-weight: 600; }

  .footer-rule { position: absolute; left: 0; bottom: 0; width: 900px; height: 8px; background: var(--red); }
</style>
</head>
<body>
<main class="flyer">
  <div class="hero-photo" role="img" aria-label="Smiling retired couple on a bicycle among golden autumn trees"></div>
  <div class="hero-rule"></div>

  <div class="brand">
    <span class="brand-dot"></span>
    <div class="brand-name">HERONFIELD</div>
    <div class="brand-sub">WEALTH ADVISORS, INC.</div>
  </div>

  <section class="lead-box">
    <span class="bar"></span>
    <h1 class="lead-text">The most important thing to realize when leaving an employer is that you have options for the money that you have worked hard for and saved.</h1>
    <svg class="fold" viewBox="0 0 28 28"><polygon points="0,28 28,0 0,0" fill="#fff"/><polygon points="0,28 28,0 28,28" fill="#1c1c1c"/></svg>
  </section>

  <section class="body-copy">
    <p>It is important to work with a fiduciary to help you evaluate your options and the pros and cons of them. A fiduciary is someone who is obligated to provide you unbiased advice and disclose any conflicts of interest in their recommendations. It can be particularly important to work with a fiduciary if you are retiring early or are generally confused about all of the information and misinformation out there.</p>
    <p>We recommend working with an expert who has experience with a multitude of different types of qualified plans such as 401(k), 403(b), Employee Stock Ownership Plans, SEP IRAs, etc. Not all plan types are eligible for rollovers, and even if they are, they may vary in the types of plans that they can be rolled in to.</p>
  </section>

  <section class="compare">
    <div class="compare-title">Rolling over 401(k) assets to IRA</div>
    <table class="compare-table">
      <tr><th>PROS</th><th>CONS</th></tr>
      <tr class="row-a">
        <td><svg viewBox="0 0 12 12"><circle cx="6" cy="6" r="5.2" fill="none" stroke="#c8212f" stroke-width="1.2"/><path d="M3.5 6.2l1.8 1.7 3.2-3.4" fill="none" stroke="#c8212f" stroke-width="1.2"/></svg>Typically more investment choices in an IRA</td>
        <td><svg viewBox="0 0 12 12"><circle cx="6" cy="6" r="5.2" fill="none" stroke="#c8212f" stroke-width="1.2"/><path d="M3.5 6.2l1.8 1.7 3.2-3.4" fill="none" stroke="#c8212f" stroke-width="1.2"/></svg>Less protection from creditors</td>
      </tr>
      <tr class="row-b">
        <td><svg viewBox="0 0 12 12"><circle cx="6" cy="6" r="5.2" fill="none" stroke="#c8212f" stroke-width="1.2"/><path d="M3.5 6.2l1.8 1.7 3.2-3.4" fill="none" stroke="#c8212f" stroke-width="1.2"/></svg>Ability to make contributions to the account even after leaving your former employer</td>
        <td><svg viewBox="0 0 12 12"><circle cx="6" cy="6" r="5.2" fill="none" stroke="#c8212f" stroke-width="1.2"/><path d="M3.5 6.2l1.8 1.7 3.2-3.4" fill="none" stroke="#c8212f" stroke-width="1.2"/></svg>Less access to funds prior to age 59½</td>
      </tr>
      <tr class="row-c">
        <td><svg viewBox="0 0 12 12"><circle cx="6" cy="6" r="5.2" fill="none" stroke="#c8212f" stroke-width="1.2"/><path d="M3.5 6.2l1.8 1.7 3.2-3.4" fill="none" stroke="#c8212f" stroke-width="1.2"/></svg>Choice of investment custodian and investment advisor you work with</td>
        <td><svg viewBox="0 0 12 12"><circle cx="6" cy="6" r="5.2" fill="none" stroke="#c8212f" stroke-width="1.2"/><path d="M3.5 6.2l1.8 1.7 3.2-3.4" fill="none" stroke="#c8212f" stroke-width="1.2"/></svg>RMDs on funds at age 72 regardless if you are still working</td>
      </tr>
    </table>
  </section>

  <article class="option opt-leave"><h2>Leave it</h2><p>Most employer plans allow you to leave the funds within the qualified plan</p></article>
  <article class="option opt-roll"><h2>Roll it</h2><p>Depending on the type of qualified plan, you can roll the funds over from the employer plan to an IRA.</p></article>
  <article class="option opt-move"><h2>Move it</h2><p>If you’ve started working at a new company, they will often have their own qualified plan available that you can move your old company’s funds to.</p></article>
  <article class="option opt-take"><h2>Take it</h2><p>There is the option to take the account in cash, but it is not typically advisable due to the tax and potential penalty implications.</p></article>

  <div class="cta">
    <svg class="cta-tab" width="307" height="40" viewBox="0 0 307 40"><polygon points="0,0 168,0 193,39 0,39" fill="#c8212f"/><rect x="0" y="38" width="307" height="1.5" fill="#c8212f"/></svg>
    <span class="cta-label">talk to us</span>
  </div>
  <div class="phone">
    <svg viewBox="0 0 28 28"><circle cx="14" cy="14" r="12.5" fill="none" stroke="#c8212f" stroke-width="2"/><path d="M10 7.5l2.6 3-1.6 2c.9 1.9 2.4 3.4 4.3 4.3l2-1.6 3 2.6-1.6 2.3c-4.8.4-11.7-6.5-11.3-11.3z" fill="#c8212f"/></svg>
    <span>919-555-0186</span>
  </div>
  <div class="website">www.<strong>GrowWithHeronfield</strong>.com</div>

  <div class="footer-rule"></div>
</main>
</body>
</html>
```